Bref créative
Businesscard + stationary
outstand and cretive master piece!
Bright & Fun-filled
Mariana Tolvaldi
www.pixelharbor-exemplo.com.br
contato@pixelharbor-exemplo.com.br
You need to add to business card:
Skype: pixelharbor.online
Twitter: @PixelHarboron
Secondary text to go below logo: Desenvolvimento Web
On the back of business card goes only the logo and some nice art if applyable
This is the new website layout, so please follow this style to create the businesscard and stationary.
This is teh original logo file in EPS
this is another version of teh logo

```html
<!DOCTYPE html>
<html lang="pt-BR">
<head>
<meta charset="utf-8">
<title>pixelharbor — Cartão de visita</title>
<link rel="stylesheet" href="https://fonts.googleapis.com/css2?family=Comfortaa:wght@400;600&family=Open+Sans:wght@400;600&display=swap">
<style>
  :root {
    --page: #e6e6e4;
    --card: #141414;
    --accent: #4a9ad8;
    --text-light: #f2f2f2;
    --text-muted: #cfcfcf;
  }
  * { box-sizing: border-box; margin: 0; padding: 0; }
  html, body { width: 1200px; height: 901px; overflow: hidden; }
  body {
    background: var(--page);
    font-family: "Open Sans", Arial, sans-serif;
    position: relative;
  }
  .card {
    position: absolute;
    width: 520px;
    height: 300px;
    background: var(--card);
    overflow: hidden;
  }
  /* Front */
  .card-front {
    left: 70px; top: 150px;
    border-radius: 0 60px 0 0;
    background: var(--accent);
  }
  .card-front .panel {
    position: absolute;
    left: 0; top: 0;
    width: 506px; height: 288px;
    background: var(--card);
    border-radius: 0 50px 0 0;
  }
  .card-front .accent-dot {
    position: absolute;
    right: 28px; top: 22px;
    width: 36px; height: 36px;
    border-radius: 50%;
    background: var(--accent);
  }
  .brand-name {
    font-family: "Comfortaa", "Open Sans", sans-serif;
    font-weight: 600;
    color: var(--text-light);
    letter-spacing: -0.5px;
    line-height: 1;
  }
  .brand-tagline {
    color: var(--accent);
    font-size: 13px;
    margin-top: 4px;
  }
  .card-front .brand { position: absolute; left: 34px; top: 62px; }
  .card-front .brand-name { font-size: 40px; }
  .holder-name {
    position: absolute;
    left: 300px; top: 105px;
    color: var(--accent);
    font-size: 18px;
    font-weight: 600;
    line-height: 1.3;
    text-align: center;
  }
  .contact-list {
    position: absolute;
    left: 34px; top: 196px;
    list-style: none;
    color: var(--text-muted);
    font-size: 11px;
    line-height: 16px;
  }
  .contact-list li { display: flex; align-items: center; gap: 8px; }
  .contact-list svg { width: 10px; height: 10px; fill: var(--accent); }
  /* Back */
  .card-back {
    left: 610px; top: 420px;
    border-radius: 0 0 0 60px;
  }
  .card-back .brand {
    position: absolute;
    left: 0; right: 0; top: 92px;
    text-align: center;
  }
  .card-back .brand-name { font-size: 58px; }
  .card-back .brand-tagline { font-size: 17px; margin-top: 6px; }
  .social-row {
    position: absolute;
    left: 80px; bottom: 26px;
    display: flex; gap: 26px;
    color: var(--text-muted);
    font-size: 11px;
  }
  .social-row span { display: flex; align-items: center; gap: 6px; }
  .social-mark {
    width: 12px; height: 12px;
    background: var(--accent);
    border-radius: 2px;
  }
</style>
</head>
<body>
  <section class="card card-front" aria-label="Frente do cartão">
    <div class="panel"></div>
    <div class="accent-dot"></div>
    <div class="brand">
      <div class="brand-name">pixelharbor</div>
      <div class="brand-tagline">Desenvolvimento Web</div>
    </div>
    <div class="holder-name">Mariana<br>Tolvaldi</div>
    <ul class="contact-list">
      <li><svg viewBox="0 0 10 10"><path d="M2 0h2l1 3-1.5 1a6 6 0 0 0 2.5 2.5L7 5l3 1v2a2 2 0 0 1-2 2A8 8 0 0 1 0 2a2 2 0 0 1 2-2z"/></svg>11 3000 0101</li>
      <li><svg viewBox="0 0 10 10"><rect x="2" y="0" width="6" height="10" rx="1"/></svg>11 9000 0202</li>
      <li><svg viewBox="0 0 10 10"><path d="M0 2h10v6H0z"/></svg>contato@pixelharbor-exemplo.com.br</li>
      <li><svg viewBox="0 0 10 10"><circle cx="5" cy="5" r="5"/></svg>www.pixelharbor-exemplo.com.br</li>
    </ul>
  </section>

  <section class="card card-back" aria-label="Verso do cartão">
    <div class="brand">
      <div class="brand-name">pixelharbor</div>
      <div class="brand-tagline">Desenvolvimento Web</div>
    </div>
    <div class="social-row">
      <span><i class="social-mark"></i>pixelharbor.online</span>
      <span><i class="social-mark"></i>@PixelHarboron</span>
    </div>
  </section>
</body>
</html>
```